Business Card Design Project : Tidewell Press

In preparation for market launch, Whistler's Tidewell Press require the development of a business card. Tidewell Press is a Community online publishing web portal. We provide the the city of Whistler located in B.C. (Canada) business directories, News, Classified ads, News, Events and blogs etc.

The main focus of the brand is to help local businesses to corporate with their online advertisement and marketing. Meeting our clients face to face is a must (B2B).

Target Market(s)

The target market is B2B customers. Business Owners to Marketing, advertising Managers

Industry/Entity Type

Business

Requirements
Must have
• - The business card will be two sided.
the BACK side will have our logo which consist of (icon, url,slogan) submited. The logo will be middle and centred.

The FRONT side should have company details:

Company Legal Name: FERNDALE TIDEWELL PRESS

Owen Marsk
Director of Sales & Marketing

www.ferndaletidewell.biz
owen@ferndaletidewell.biz

Phone: 555 014 3826
#2817 - 562 E. Harlow Ave.
Vancouver, B.C. K7P2R4 Canada
Nice to have
• - For the "FRONT" side of our business card. You can separate or re-arrange with our logo components (icon, logo,slogan). It does not have to be together.

Also our company legal name is rather long so arrange or organize the name in a way to make it shorter. Your experience and creativity will have to come in play.
Should not have
• should not have other colors beside logo color and black text (2 colors). Also nothing Three dimensional

```html
<!DOCTYPE html>
<html lang="en">
<head>
<meta charset="utf-8">
<title>Tidewell Press — Business Card</title>
<link rel="stylesheet" href="https://fonts.googleapis.com/css2?family=Source+Sans+3:wght@400;600;700&display=swap">
<style>
  :root {
    --backdrop: #2b2b2b;
    --card: #ffffff;
    --brand-blue: #0a7cc4;
    --ink: #2a2a2a;
    --ink-soft: #555555;
    --font: "Source Sans 3", Arial, sans-serif;
  }
  * { box-sizing: border-box; margin: 0; padding: 0; }
  html, body {
    width: 1200px; height: 798px; overflow: hidden;
    background: var(--backdrop);
    font-family: var(--font);
  }
  .canvas { position: relative; width: 1200px; height: 798px; }
  .card {
    position: absolute; width: 515px; height: 294px;
    background: var(--card);
  }
  .card--back { left: 216px; top: 92px; text-align: center; }
  .card--front { left: 473px; top: 415px; }

  /* Back side */
  .brand-mark {
    position: absolute; left: 0; right: 0; top: 86px;
    display: flex; justify-content: center; align-items: center; gap: 10px;
    color: var(--brand-blue); font-weight: 700; font-size: 36px; line-height: 1;
  }
  .brand-mark__dot {
    width: 18px; height: 18px; border-radius: 50%; background: var(--brand-blue);
  }
  .brand-url {
    position: absolute; left: 0; right: 0; top: 160px;
    color: var(--ink); font-weight: 700; font-size: 22px; letter-spacing: -0.2px;
  }
  .brand-slogan {
    position: absolute; left: 0; right: 0; top: 186px;
    color: var(--brand-blue); font-weight: 400; font-size: 17px;
  }

  /* Front side */
  .company-name {
    position: absolute; left: 70px; top: 70px;
    color: var(--brand-blue); font-weight: 700; font-size: 33px; line-height: 31px;
    letter-spacing: -0.3px;
  }
  .contact { position: absolute; left: 303px; top: 134px; color: var(--ink-soft); }
  .contact__name { color: var(--ink); font-weight: 700; font-size: 14px; line-height: 16px; }
  .contact__title { color: var(--ink); font-weight: 600; font-size: 11px; line-height: 14px; }
  .contact__block { margin-top: 22px; font-size: 10.5px; line-height: 14px; }
  .contact__block + .contact__block { margin-top: 7px; }
  .contact__web { margin-top: 6px; font-size: 10.5px; line-height: 14px; }
</style>
</head>
<body>
<main class="canvas">
  <section class="card card--back" aria-label="Card back">
    <div class="brand-mark"><span class="brand-mark__dot"></span>Tidewell Press</div>
    <p class="brand-url">www.ferndaletidewell.biz</p>
    <p class="brand-slogan">Your information gateway</p>
  </section>

  <section class="card card--front" aria-label="Card front">
    <h1 class="company-name">ferndale<br>tidewell<br>press</h1>
    <div class="contact">
      <p class="contact__name">Owen Marsk</p>
      <p class="contact__title">Director of Sales &amp; Marketing</p>
      <p class="contact__block">#2817 - 562 E. Harlow Ave.<br>Vancouver, B.C. K7P2R4 Canada</p>
      <p class="contact__block">Phone: 555 014 3826<br>Email: owen@ferndaletidewell.biz</p>
      <p class="contact__web">www.ferndaletidewell.biz</p>
    </div>
  </section>
</main>
</body>
</html>
```